Pause Often, Now Discover Poster for Fernvale Stacks Keepers

Task Description
I am the Vice President of Advocacy for the Fernvale Stacks Keepers Association. I am looking to have a set of posters made for POND (Pause Often, Now Discover) in October. POND is a time when all school children in BC are encouraged to Pause Often, Now Discover for 15-20 minutes at some point in their day.

I would like to get a set of 2 digital posters designed (if possible it would be nice to have the option to print to both 11x17 and 8.5x 11 paper). We need a poster that is high school (Grade 8-12) appropriate and one that is elementary (Grade k-7) appropriate. Both posters need to be replicated in French. All posters need to have the FOMU logo on them as well as the Fernvale Stacks Keepers Association Logo.

My budget is not huge (whose is?), but we are flexible and open with design. We want posters that appeal to the age groups they are designed for and that promote reading. We would require the digital copy by August 20. Schools will arrange for their own printing as distribution to all the schools in BC is laborious.

Each poster needs to have the following information:

-Pause Often, Now Discover (POND)
- A Blank Spot that we can add a date to
-the logo for the FOMU (attached)
-the logo for the FSKA (attached)- the logos do not have to be large.

Industry/Entity Type

Teacher

Font styles to use
Serif

Requirements
Must have
• -Pause Often, Now Discover (POND)
• - A Blank Spot that we can add a date to
• -the logo for the FOMU (attached)
• -the logo for the FSKA (attached)- the logos do not have to be large.
Nice to have
• Clear Bright Colours
• I have attached last year's posters to give an idea of what we are interested in.

```html
<!DOCTYPE html>
<html lang="en">
<head>
<meta charset="utf-8">
<title>POND Poster – Fernvale Stacks Keepers Association</title>
<link rel="stylesheet" href="https://fonts.googleapis.com/css2?family=Anton&display=swap">
<style>
  :root {
    --page-bg: #3a3a3a;
    --poster-cream: #fbf0d2;
    --ink: #2e2416;
    --logo-ink: #1c1c1c;
    --logo-dot: #4f9a63;
    --date-box: #2e2415;
    --corner-tone: rgba(20, 20, 20, 0.28);
    --reader-tone: rgba(30, 24, 18, 0.35);
  }
  * { margin: 0; padding: 0; box-sizing: border-box; }
  html, body {
    width: 1200px;
    height: 1200px;
    overflow: hidden;
    background: var(--page-bg);
  }
  .poster {
    position: absolute;
    left: 224px;
    top: 20px;
    width: 752px;
    height: 1160px;
    background: var(--poster-cream);
    overflow: hidden;
    font-family: "Anton", "Arial Narrow", sans-serif;
  }
  .corner-texture {
    position: absolute;
    width: 110px;
    height: 180px;
  }
  .corner-texture.top-left { left: 0; top: 0; background: radial-gradient(ellipse at 0 0, var(--corner-tone), transparent 70%); }
  .corner-texture.top-right { right: 0; top: 0; background: radial-gradient(ellipse at 100% 0, var(--corner-tone), transparent 70%); }
  .corner-texture.bottom-left { left: 0; bottom: 0; background: radial-gradient(ellipse at 0 100%, var(--corner-tone), transparent 70%); }
  .corner-texture.bottom-right { right: 0; bottom: 0; background: radial-gradient(ellipse at 100% 100%, var(--corner-tone), transparent 70%); }

  .association-mark {
    position: absolute;
    display: flex;
    align-items: center;
    gap: 10px;
    color: var(--logo-ink);
    line-height: 1;
  }
  .association-mark.fska { left: 118px; top: 60px; font-size: 62px; }
  .association-mark.fomu { left: 536px; top: 66px; font-size: 30px; }
  .association-mark .mark-dot {
    border-radius: 50%;
    flex: none;
  }
  .association-mark.fska .mark-dot { width: 40px; height: 40px; background: var(--logo-dot); }
  .association-mark.fomu .mark-dot { width: 44px; height: 44px; background: var(--logo-ink); }

  .young-readers {
    position: absolute;
    left: 56px;
    top: 172px;
    width: 640px;
    height: 192px;
    border-radius: 10px;
    background: linear-gradient(180deg, rgba(30,24,18,0.06), var(--reader-tone));
  }

  .title-block {
    position: absolute;
    left: 0;
    top: 0;
    width: 752px;
    height: 1160px;
  }

  .date-slot {
    position: absolute;
    left: 202px;
    top: 899px;
    width: 340px;
    height: 84px;
    border-radius: 6px;
    background: var(--date-box);
  }
</style>
</head>
<body>
  <main class="poster">
    <div class="corner-texture top-left" role="img" aria-label="Halftone dot texture in the corner"></div>
    <div class="corner-texture top-right" role="img" aria-label="Halftone dot texture in the corner"></div>
    <div class="corner-texture bottom-left" role="img" aria-label="Halftone dot texture in the corner"></div>
    <div class="corner-texture bottom-right" role="img" aria-label="Halftone dot texture in the corner"></div>

    <div class="association-mark fska"><span class="mark-dot"></span><span>FSKA</span></div>
    <div class="association-mark fomu"><span class="mark-dot"></span><span>FOMU</span></div>

    <div class="young-readers" role="img" aria-label="Silhouettes of children reading books, standing and lying on top of the title letters"></div>

    <svg class="title-block" viewBox="0 0 752 1160" aria-labelledby="pond-title">
      <defs>
        <linearGradient id="bookshelf-rainbow" x1="0" y1="375" x2="0" y2="790" gradientUnits="userSpaceOnUse">
          <stop offset="0" stop-color="#e0243a"/>
          <stop offset="0.2" stop-color="#f07a22"/>
          <stop offset="0.4" stop-color="#f5d21c"/>
          <stop offset="0.6" stop-color="#3aa64a"/>
          <stop offset="0.8" stop-color="#2a8fd6"/>
          <stop offset="1" stop-color="#8a4aa8"/>
        </linearGradient>
      </defs>
      <text id="pond-title" class="pond-word" x="44" y="790" font-family="Anton, 'Arial Narrow', sans-serif" font-size="480" fill="url(#bookshelf-rainbow)" textLength="665" lengthAdjust="spacingAndGlyphs">POND</text>
      <text class="pond-tagline" x="44" y="867" font-family="Anton, 'Arial Narrow', sans-serif" font-size="65" fill="var(--ink)" textLength="669" lengthAdjust="spacingAndGlyphs">PAUSE OFTEN, NOW DISCOVER</text>
    </svg>

    <div class="date-slot" aria-label="Space for the event date"></div>
  </main>
</body>
</html>
```